Property developer, money partner needs business card design using logo concept provided

Our company develops residential properties, does money lends for joint ventures in property deals and finds property deals for other money partners. We have provided a basic logo for you to work from. Any graphic or logo design on the card is to communicate development and finance collaboration. Color choice is not so important for us, but color choice does need to reflect professionalism.

```html
<!DOCTYPE html>
<html lang="en">
<head>
<meta charset="utf-8">
<title>Keystead Property Solutions – Business Card</title>
<link href="https://fonts.googleapis.com/css2?family=Arimo:wght@400;700&display=swap" rel="stylesheet">
<style>
  :root {
    --stage: #3b3b3d;
    --brand-blue: #0a57a8;
    --brand-blue-light: #0f78c4;
    --brand-blue-dark: #064a92;
    --accent-red: #a30f16;
    --ink: #333333;
    --rule: #8a8a8a;
    --paper: #ffffff;
    --faint: #eef3f9;
  }
  * { margin: 0; padding: 0; box-sizing: border-box; }
  html, body { width: 1200px; height: 689px; overflow: hidden; }
  body {
    background: var(--stage);
    font-family: "Arimo", Arial, sans-serif;
    position: relative;
  }
  .card {
    position: absolute;
    top: 190px;
    width: 540px;
    height: 309px;
    border-radius: 18px;
    overflow: hidden;
  }
  /* Back side */
  .card-back {
    left: 40px;
    background: linear-gradient(135deg, var(--brand-blue-light), var(--brand-blue-dark));
  }
  .card-back .brand {
    position: absolute;
    left: 0; right: 0; top: 110px;
    text-align: center;
    color: #0a5fae;
  }
  .card-back .brand-name {
    font-size: 30px;
    font-weight: 700;
    letter-spacing: 5px;
    text-transform: uppercase;
  }
  .card-back .brand-sub {
    margin-top: 6px;
    font-size: 15px;
    font-weight: 700;
    letter-spacing: 3px;
  }
  .card-back .brand-reg {
    margin-top: 4px;
    font-size: 9px;
    letter-spacing: 2px;
  }

  /* Front side */
  .card-front {
    left: 620px;
    background: var(--paper);
  }
  .watermark {
    position: absolute;
    left: 30px; top: 110px;
    width: 190px; height: 190px;
    border-radius: 50%;
    background: var(--faint);
  }
  .front-brand {
    position: absolute;
    right: 26px; top: 28px;
    display: flex;
    align-items: center;
    gap: 10px;
    color: var(--brand-blue);
  }
  .front-brand .mark {
    width: 44px; height: 44px;
    border-radius: 50%;
    background: var(--brand-blue);
  }
  .front-brand .brand-name {
    font-size: 20px;
    font-weight: 700;
    letter-spacing: 3px;
    line-height: 1.1;
  }
  .front-brand .brand-sub {
    font-size: 10px;
    letter-spacing: 1.5px;
    color: var(--ink);
  }
  .front-rule {
    position: absolute;
    right: 26px; top: 94px;
    width: 300px;
    height: 1px;
    background: var(--rule);
  }
  .address {
    position: absolute;
    right: 26px; top: 112px;
    text-align: right;
    font-size: 13px;
    line-height: 1.4;
    color: var(--ink);
  }
  .person {
    position: absolute;
    left: 30px; top: 150px;
  }
  .person-name {
    font-size: 22px;
    font-weight: 700;
    color: var(--brand-blue);
    text-transform: uppercase;
  }
  .person-role {
    font-size: 13px;
    color: var(--accent-red);
    margin-top: 2px;
  }
  .person-rule {
    width: 180px;
    height: 1px;
    background: var(--rule);
    margin: 8px 0;
  }
  .contacts { list-style: none; }
  .contacts li {
    display: flex;
    align-items: center;
    gap: 10px;
    font-size: 13px;
    color: var(--ink);
    line-height: 1.5;
  }
  .contacts svg { width: 12px; height: 12px; fill: var(--accent-red); flex: none; }
  .bands { position: absolute; left: 0; top: 0; width: 540px; height: 309px; }
  .website {
    position: absolute;
    right: 22px; bottom: 22px;
    font-size: 13px;
    color: var(--paper);
  }
</style>
</head>
<body>
  <section class="card card-back" aria-label="Card back">
    <div class="brand">
      <div class="brand-name">Keystead</div>
      <div class="brand-sub">Property Solutions</div>
      <div class="brand-reg">A.C.N 418 207 356</div>
    </div>
  </section>

  <section class="card card-front" aria-label="Card front">
    <div class="watermark" aria-hidden="true"></div>

    <div class="front-brand">
      <span class="mark" aria-hidden="true"></span>
      <div>
        <div class="brand-name">KEYSTEAD</div>
        <div class="brand-sub">Property Solutions · A.C.N 418 207 356</div>
      </div>
    </div>
    <div class="front-rule"></div>

    <address class="address" style="font-style:normal">
      2140 Alder Ridge Road<br>
      Fairview, Oregon 97024
    </address>

    <div class="person">
      <div class="person-name">Daniel Morrow</div>
      <div class="person-role">Managing Director</div>
      <div class="person-rule"></div>
      <ul class="contacts">
        <li>
          <svg viewBox="0 0 24 24" aria-hidden="true"><path d="M6.6 10.8a15 15 0 0 0 6.6 6.6l2.2-2.2a1 1 0 0 1 1-.25 11.4 11.4 0 0 0 3.6.57 1 1 0 0 1 1 1V20a1 1 0 0 1-1 1A17 17 0 0 1 3 4a1 1 0 0 1 1-1h3.5a1 1 0 0 1 1 1c0 1.25.2 2.45.57 3.57a1 1 0 0 1-.25 1z"/></svg>
          555-210-4871
        </li>
        <li>
          <svg viewBox="0 0 24 24" aria-hidden="true"><path d="M7 1h10a2 2 0 0 1 2 2v18a2 2 0 0 1-2 2H7a2 2 0 0 1-2-2V3a2 2 0 0 1 2-2zm0 3v14h10V4zm5 15.5a1 1 0 1 0 0 2 1 1 0 0 0 0-2z"/></svg>
          555-390-6128
        </li>
        <li>
          <svg viewBox="0 0 24 24" aria-hidden="true"><path d="M2 5h20v14H2zm2 2v.5l8 5 8-5V7zm0 2.8V17h16V9.8l-8 5z"/></svg>
          info@keysteadgroup.com
        </li>
      </ul>
    </div>

    <svg class="bands" viewBox="0 0 540 309" aria-hidden="true">
      <polygon points="0,296 355,252 365,252 365,262 0,309" fill="var(--accent-red)"/>
      <polygon points="0,309 365,262 540,262 540,309" fill="var(--accent-red)" opacity="0"/>
      <polygon points="340,309 362,246 540,222 540,309" fill="var(--brand-blue)"/>
      <polygon points="0,309 362,258 362,309" fill="var(--accent-red)"/>
    </svg>
    <div class="website">www.keysteadgroup.com</div>
  </section>
</body>
</html>
```